Carrowell Business Card Re-design

Our current cards are outdated. This is our website www.carrowellinsights.example. We would like something that is "on-brand" and consistent with our social media sites. We are strategic consultants with a core competency in Marketing Research. Although, please know we are considering a brand logo redesign and potentially a new look. If we like your work here we will invite you to participate when we get to that project. Thank you very much. Harriet
Here are our social sites: https://twitter.com/Carrowell?lang=en
https://plus.google.com/+Carrowellinsights
https://www.linkedin.com/company/5094827/
https://www.facebook.com/CarrowellInc/
Business

```html
<!DOCTYPE html>
<html lang="en">
<head>
<meta charset="utf-8">
<title>Carrowell Business Card</title>
<link rel="stylesheet" href="https://fonts.googleapis.com/css2?family=Montserrat:wght@400;500;700&display=swap">
<style>
  :root {
    --backdrop: #a8cc8c;
    --card: #ffffff;
    --brand-green: #6cbf45;
    --brand-green-soft: #e6f2df;
    --ink: #231f20;
    --text: #2b2b2b;
  }
  html, body {
    margin: 0;
    padding: 0;
    width: 1200px;
    height: 800px;
    overflow: hidden;
    background: var(--backdrop);
    font-family: "Montserrat", sans-serif;
  }
  .canvas {
    position: relative;
    width: 1200px;
    height: 800px;
  }
  .card {
    position: absolute;
    top: 283px;
    width: 430px;
    height: 239px;
    background: var(--card);
    overflow: hidden;
  }
  .card--front { left: 110px; }
  .card--back { left: 638px; }

  .brand-motif {
    position: absolute;
    background: linear-gradient(135deg, var(--ink) 0%, var(--ink) 45%, var(--brand-green) 100%);
  }
  .brand-motif--front { left: 304px; top: 0; width: 126px; height: 239px; }
  .brand-motif--back-left {
    left: 0; top: 0; width: 138px; height: 239px;
    background: linear-gradient(225deg, var(--ink) 0%, var(--ink) 45%, var(--brand-green) 100%);
  }
  .brand-motif--back-corner { left: 370px; top: 162px; width: 60px; height: 77px; background: var(--ink); }
  .brand-motif--faint {
    left: 2px; top: 59px; width: 124px; height: 106px;
    background: var(--brand-green-soft);
  }

  .wordmark {
    position: absolute;
    margin: 0;
    color: var(--brand-green);
    font-weight: 500;
    letter-spacing: -0.5px;
    line-height: 1;
  }
  .card--front .wordmark {
    left: 12px;
    top: 10px;
    font-size: 46px;
  }
  .card--back .wordmark {
    left: 144px;
    top: 84px;
    font-size: 56px;
  }

  .holder {
    position: absolute;
    left: 93px;
    top: 127px;
    width: 110px;
    text-align: right;
  }
  .holder__name {
    margin: 0;
    font-size: 14px;
    font-weight: 400;
    color: var(--ink);
    text-align: left;
    letter-spacing: 0.3px;
    line-height: 1;
  }
  .holder__role {
    margin: 2px 0 0;
    font-size: 9.5px;
    font-weight: 700;
    color: var(--brand-green);
    letter-spacing: 0.3px;
  }

  .contact-list {
    position: absolute;
    left: 93px;
    top: 169px;
    margin: 0;
    padding: 0;
    list-style: none;
  }
  .contact-list__item {
    display: flex;
    align-items: center;
    height: 14.5px;
    font-size: 10.5px;
    color: var(--text);
  }
  .contact-list__icon {
    width: 10px;
    height: 10px;
    margin-right: 9px;
    flex: none;
  }
</style>
</head>
<body>
<main class="canvas">

  <section class="card card--front" aria-label="Business card front">
    <div class="brand-motif brand-motif--faint" role="img" aria-label="Faint brand arrow decoration area"></div>
    <div class="brand-motif brand-motif--front" role="img" aria-label="Large brand symbol decoration area in charcoal and green"></div>

    <h1 class="wordmark">Carrowell</h1>

    <div class="holder">
      <p class="holder__name">LOREM IPSUM</p>
      <p class="holder__role">DOLOR SIT</p>
    </div>

    <ul class="contact-list">
      <li class="contact-list__item">
        <svg class="contact-list__icon" viewBox="0 0 10 10" fill="none" stroke="#6cbf45" stroke-width="0.9">
          <path d="M2 1 L3.5 1 L4.2 3 L3.2 3.8 Q4 5.8 6.2 6.8 L7 5.8 L9 6.5 L9 8 Q8.5 9 7.5 9 Q2.5 8 1 2.5 Q1 1.5 2 1 Z"/>
        </svg>
        +1 111 222 333
      </li>
      <li class="contact-list__item">
        <svg class="contact-list__icon" viewBox="0 0 10 10" fill="none" stroke="#6cbf45" stroke-width="0.9">
          <rect x="0.5" y="2" width="9" height="6.5"/>
          <path d="M0.5 2 L5 5.5 L9.5 2"/>
        </svg>
        hello@carrowellinsights.example
      </li>
      <li class="contact-list__item">
        <svg class="contact-list__icon" viewBox="0 0 10 10" fill="none" stroke="#6cbf45" stroke-width="0.9">
          <path d="M5 9.5 Q1.5 5.5 1.5 3.8 A3.5 3.5 0 0 1 8.5 3.8 Q8.5 5.5 5 9.5 Z"/>
          <circle cx="5" cy="3.8" r="1.2"/>
        </svg>
        12345, Fake Street
      </li>
      <li class="contact-list__item">
        <svg class="contact-list__icon" viewBox="0 0 10 10" fill="none" stroke="#6cbf45" stroke-width="0.9">
          <circle cx="5" cy="5" r="4.3"/>
          <ellipse cx="5" cy="5" rx="1.8" ry="4.3"/>
          <path d="M0.7 5 H9.3"/>
        </svg>
        www.carrowellinsights.example
      </li>
    </ul>
  </section>

  <section class="card card--back" aria-label="Business card back">
    <div class="brand-motif brand-motif--back-left" role="img" aria-label="Large brand symbol decoration area in charcoal and green"></div>
    <div class="brand-motif brand-motif--back-corner" role="img" aria-label="Corner brand symbol decoration area in charcoal"></div>
    <p class="wordmark">Carrowell</p>
  </section>

</main>
</body>
</html>
```